Webshop for furniture and lamps

We need a design for a web shop with APP that should have two options:
1-Webshop in general which should attract to private customer in general and
2-Website that is meant to attract big customers as hotels and restaurants who would have their own customerize login.

That's the idea behind the shop.

It should be diveded into 4 parts
vintage furniture
rattan set outdoor and indoor
lamps and
wooden wall decor

The name of the shop is brisa novelta!

Please kindly make me an offer.

Reason: Dear designers, so far there hasn't been a design that really matched. Look up German web sites like www.fernblick-art.de or www.holzkante17.de... Haven't been convinced by designs! Sorry folks. Please submit some new ones. Kind regards Ned

```html
<!DOCTYPE html>
<html lang="en">
<head>
<meta charset="utf-8">
<title>Brisa Novelta – Furniture &amp; Lamps</title>
<link rel="stylesheet" href="https://fonts.googleapis.com/css2?family=Oswald:wght@500;600&family=Roboto+Condensed:wght@700&family=Arimo:wght@400;700&display=swap">
<style>
  :root {
    --bar: #222222;
    --ink-dark: #0d0d0d;
    --orange: #e8700f;
    --orange-soft: #f0954a;
    --amber: #f5a623;
    --white: #ffffff;
    --link-blue: #1ea7e6;
    --sale-red: #ee1c24;
    --price-brown: #8b2b14;
    --tag-teal: #2d7a8c;
    --tag-olive: #3b3a2e;
    --tag-rust: #7a2e12;
    --footer-brown: #7a3a10;
    --body-grey: #e6e6e6;
  }
  * { box-sizing: border-box; }
  html, body {
    margin: 0; padding: 0;
    width: 1167px; height: 1200px;
    overflow: hidden;
    background: var(--white);
    font-family: "Arimo", Arial, sans-serif;
  }
  .page { position: relative; width: 1167px; height: 1200px; overflow: hidden; }

  /* Header */
  .site-header { position: absolute; top: 0; left: 0; width: 1167px; height: 113px; background: var(--bar); z-index: 3; }
  .brand-tab {
    position: absolute; left: 0; top: 0; width: 340px; height: 150px;
    background: var(--bar); border-radius: 0 0 170px 170px / 0 0 40px 40px; z-index: 4;
  }
  .brand {
    position: absolute; left: 40px; top: 38px; display: flex; align-items: center; gap: 14px;
  }
  .brand-dot { width: 46px; height: 46px; border-radius: 50%; background: var(--orange-soft); }
  .brand-name {
    font-family: "Oswald", sans-serif; font-weight: 500; font-size: 34px; line-height: 38px;
    color: var(--amber); text-transform: uppercase; letter-spacing: 1px; width: 170px;
  }
  .utility { position: absolute; top: 7px; font-family: "Roboto Condensed", sans-serif; font-weight: 700; font-size: 15px; color: var(--link-blue); }
  .utility.follow { left: 755px; display: flex; align-items: center; gap: 8px; }
  .utility.follow .dot { width: 14px; height: 14px; border-radius: 50%; background: var(--link-blue); }
  .utility.checkout { left: 940px; display: flex; align-items: center; gap: 10px; }
  .main-nav { position: absolute; top: 40px; left: 0; width: 1167px; height: 47px; }
  .main-nav a {
    position: absolute; top: 0; height: 47px; line-height: 47px;
    font-family: "Roboto Condensed", sans-serif; font-weight: 700; font-size: 19px; color: var(--white); text-decoration: none;
  }
  .main-nav a.active { background: var(--orange); padding: 0 17px; border-radius: 6px 6px 0 0; }

  .dropdown {
    position: absolute; left: 677px; top: 87px; width: 260px; height: 137px;
    background: var(--orange); z-index: 5; box-shadow: 0 3px 8px rgba(0,0,0,.35);
    padding: 12px 0 0 14px;
  }
  .dropdown ul { margin: 0; padding: 0 0 0 30px; color: var(--white); }
  .dropdown li { font-family: "Roboto Condensed", sans-serif; font-weight: 700; font-size: 18px; line-height: 25px; white-space: nowrap; }

  /* Hero */
  .hero {
    position: absolute; left: 0; top: 113px; width: 1167px; height: 780px;
    background: linear-gradient(180deg, #b9d2e8 0%, #d6e3ee 28%, #9fb07a 40%, #6d8a3c 50%, #8c7b5e 62%, #857460 72%, #b1a796 82%, #c9c1b3 100%);
  }
  .hanger { position: absolute; top: 0; width: 3px; background: #b8b080; }
  .tag {
    position: absolute; font-family: "Oswald", sans-serif; font-weight: 600; color: var(--white);
    text-transform: uppercase; display: flex; align-items: center; justify-content: center;
    box-shadow: 3px 4px 6px rgba(0,0,0,.35);
  }
  .tag.quality { left: 180px; top: 107px; width: 196px; height: 60px; background: var(--tag-teal); font-size: 36px; }
  .tag.modern { left: 43px; top: 190px; width: 197px; height: 64px; background: var(--tag-olive); font-size: 38px; }
  .tag.comfort { left: 267px; top: 238px; width: 220px; height: 62px; background: var(--tag-rust); font-size: 34px; }

  .offer { position: absolute; left: 948px; top: 40px; font-family: "Arimo", sans-serif; }
  .offer .percent { font-size: 80px; line-height: 90px; color: var(--sale-red); }
  .offer .off { font-size: 32px; line-height: 36px; color: var(--sale-red); margin-top: 6px; }
  .offer .price { font-size: 36px; line-height: 44px; color: var(--price-brown); margin-top: 4px; }
  .add-btn {
    position: absolute; left: 1069px; top: 197px; width: 76px; height: 26px;
    background: var(--link-blue); color: var(--white); font-weight: 700; font-size: 16px;
    display: flex; align-items: center; justify-content: center;
  }
  .slider-dots {
    position: absolute; left: 811px; top: 864px; width: 332px; height: 30px;
    background: var(--ink-dark); border-radius: 12px 12px 0 0; z-index: 2;
    display: flex; align-items: center; justify-content: center; gap: 18px;
  }
  .slider-dots span { width: 17px; height: 17px; border-radius: 50%; background: var(--white); }
  .slider-dots span.current { background: var(--orange-soft); }

  /* Category strip */
  .categories {
    position: absolute; left: 0; top: 893px; width: 1167px; height: 254px;
    background: linear-gradient(180deg, #111 0%, #1e1e1e 60%, #111 100%);
  }
  .category { position: absolute; top: 0; height: 254px; }
  .category + .category { border-left: 2px solid #2e2e2e; }
  .category h2 {
    position: absolute; margin: 0; top: 20px; white-space: nowrap;
    font-family: "Oswald", sans-serif; font-weight: 600; font-size: 26px; line-height: 30px;
    text-transform: uppercase; display: flex; align-items: center; gap: 10px;
  }
  .category h2 .dot { width: 28px; height: 28px; border-radius: 50%; background: var(--orange-soft); }
  .category h2 .lead { color: var(--amber); }
  .category h2 .rest { color: var(--white); }
  .category p { position: absolute; margin: 0; color: var(--body-grey); font-size: 13px; line-height: 16.5px; }
  .read-more { position: absolute; color: var(--link-blue); font-weight: 700; font-size: 12.5px; text-decoration: none; }
  .frame { position: absolute; background: #050505; }
  .photo { position: absolute; }

  /* Footer */
  .site-footer { position: absolute; left: 0; top: 1147px; width: 1167px; height: 53px; background: var(--orange-soft); }
  .footer-band { position: absolute; left: 0; top: 0; }
  .copyright { position: absolute; left: 40px; top: 18px; font-size: 13px; color: #5a3a22; display: flex; gap: 14px; }
  .copyright .mark { font-family: "Oswald", sans-serif; font-weight: 500; font-size: 15px; line-height: 16px; text-transform: uppercase; }
  .footer-nav { position: absolute; left: 720px; top: 17px; font-size: 13px; color: var(--white); display: flex; align-items: center; gap: 10px; }
  .footer-nav .dot { width: 16px; height: 16px; border-radius: 50%; background: var(--link-blue); }
</style>
</head>
<body>
<div class="page">

  <header class="site-header">
    <div class="utility follow">Follow us <span class="dot"></span></div>
    <div class="utility checkout">
      <svg width="26" height="20" viewBox="0 0 26 20" aria-hidden="true">
        <path d="M1 2h4l3 11h13l3-8H7" fill="none" stroke="#fff" stroke-width="2.2" stroke-linejoin="round"/>
        <circle cx="10" cy="17" r="2" fill="#fff"/><circle cx="19" cy="17" r="2" fill="#fff"/>
      </svg>
      Check Out : £ 2000
    </div>
    <nav class="main-nav">
      <a href="#" style="left:520px">Home</a>
      <a href="#" style="left:616px">About</a>
      <a href="#" class="active" style="left:693px">Categories</a>
      <a href="#" style="left:838px">Shop</a>
      <a href="#" style="left:920px">Join Us?</a>
      <a href="#" style="left:1026px">Contacts</a>
    </nav>
  </header>

  <div class="brand-tab">
    <div class="brand">
      <span class="brand-dot"></span>
      <span class="brand-name">Brisa Novelta</span>
    </div>
  </div>

  <div class="dropdown">
    <ul>
      <li>Vintage Furniture</li>
      <li>Rattan set</li>
      <li>Lamps</li>
      <li>Wooden Wall décor</li>
    </ul>
  </div>

  <section class="hero" role="img" aria-label="Outdoor rattan sofa, armchair and round table with drinks on a wooden deck, trees and sky behind">
    <span class="hanger" style="left:126px;height:190px"></span>
    <span class="hanger" style="left:215px;height:110px"></span>
    <span class="hanger" style="left:300px;height:240px"></span>
    <div class="tag quality">Quality</div>
    <div class="tag modern">Modern</div>
    <div class="tag comfort">Confortable</div>
    <div class="offer">
      <div class="percent">25%</div>
      <div class="off">OFF</div>
      <div class="price">£.999</div>
    </div>
    <div class="add-btn">ADD</div>
  </section>

  <div class="slider-dots">
    <span></span><span></span><span></span><span></span><span></span><span></span><span class="current"></span><span></span>
  </div>

  <section class="categories">
    <article class="category" style="left:0;width:291px">
      <h2 style="left:11px"><span class="dot"></span><span><span class="lead">Vintage</span> <span class="rest">Furniture</span></span></h2>
      <div class="photo" style="left:11px;top:67px;width:85px;height:73px;background:linear-gradient(135deg,#f4f4f4,#9a9a9a)" role="img" aria-label="Grey vintage armchair"></div>
      <p style="left:109px;top:63px;width:148px">Lorem ipsum dolor sit amet, consectetur adipisicing elit, sed do eiusmod tempor incididunt ut labore et dolore magna aliqua. Ut enim ad minim veniam, quis nostrud exercitation ullamco laboris nisi ut</p>
      <a class="read-more" href="#" style="left:109px;top:230px">READ MORE</a>
    </article>

    <article class="category" style="left:291px;width:290px">
      <h2 style="left:36px"><span class="dot"></span><span><span class="lead">Rattan</span> <span class="rest">Set</span></span></h2>
      <p style="left:13px;top:60px;width:110px">Lorem ipsum dolor sit amet, consectetur adipisicing elit, sed do eiusmod tempor incididunt ut labore et</p>
      <a class="read-more" href="#" style="left:13px;top:200px">READ MORE</a>
      <div class="frame" style="left:125px;top:51px;width:144px;height:176px"></div>
      <div class="photo" style="left:142px;top:75px;width:103px;height:143px;background:linear-gradient(180deg,#fafafa,#e8e8e8)" role="img" aria-label="Floor lamp with red shade"></div>
    </article>

    <article class="category" style="left:581px;width:286px">
      <h2 style="left:66px"><span class="dot"></span><span class="lead">Lamps</span></h2>
      <div class="frame" style="left:30px;top:56px;width:122px;height:171px"></div>
      <div class="photo" style="left:50px;top:77px;width:89px;height:130px;background:linear-gradient(180deg,#ffffff,#e6e6e6)" role="img" aria-label="Floor lamp with striped shade"></div>
      <p style="left:164px;top:65px;width:110px">Lorem ipsum dolor sit amet, consectetur adipisicing elit, sed do eiusmod tempor incididunt ut labore et</p>
      <a class="read-more" href="#" style="left:164px;top:206px">READ MORE</a>
    </article>

    <article class="category" style="left:867px;width:300px">
      <h2 style="left:6px"><span class="dot"></span><span><span class="lead">Wooden</span> <span class="rest">Wall Decor</span></span></h2>
      <div class="frame" style="left:70px;top:50px;width:164px;height:137px"></div>
      <div class="photo" style="left:89px;top:74px;width:124px;height:93px;background:linear-gradient(90deg,#6b6f78,#a58a70 60%,#8a5a3a)" role="img" aria-label="Bedroom with wooden wall panel"></div>
      <p style="left:14px;top:189px;width:276px">Lorem ipsum dolor sit amet, consectetur adipisicing elit, sed do eiusmod tempor incididunt ut labore et <a class="read-more" href="#" style="position:static;margin-left:14px">READ MORE</a></p>
    </article>
  </section>

  <footer class="site-footer">
    <svg class="footer-band" width="1167" height="53" viewBox="0 0 1167 53" aria-hidden="true">
      <polygon points="700,0 1167,0 1167,53 646,53" fill="var(--footer-brown)"/>
    </svg>
    <div class="copyright">All Rights Reserved. <span>© <span class="mark">Brisa Novelta</span></span></div>
    <nav class="footer-nav">
      <span>Home</span><span>|</span><span>About Us</span><span>|</span><span>Contacts</span><span>|</span><span>Categories</span><span>|</span><span>@brisa_novelta</span><span class="dot"></span>
    </nav>
  </footer>

</div>
</body>
</html>
```